ultra-minimalist business card

front (black background, matte):

samir t. kouri
writer | photographer
get@samirkouri.com

back (white background, matte):

a picture speaks a thousand words;
a word draws a thousand pictures.

www.samirkouri.com

all text should be small (white or silver - as long as it shows against the black - on the front; black or gray - as long as it shows against the white - on the back).

feel free to get creative in terms of arrangement, alignment, and font type, but remember, the overall style is minimalist, so nothing too fancy, please.

thanks.

```html
<!DOCTYPE html>
<html lang="en">
<head>
<meta charset="utf-8">
<title>samir t. kouri — business card</title>
<link rel="stylesheet" href="https://fonts.googleapis.com/css2?family=Libre+Caslon+Text&display=swap">
<style>
  :root {
    --backdrop: #e4e4e6;
    --card-black: #1f1f21;
    --card-white: #f2f2f4;
    --ink-light: #e6e6e6;
    --rule-light: #bdbdbd;
    --ink-dark: #2e2e30;
    --rule-dark: #4a4a4c;
  }
  * { margin: 0; padding: 0; box-sizing: border-box; }
  html, body {
    width: 1028px;
    height: 1200px;
    overflow: hidden;
    background: var(--backdrop);
    font-family: "Libre Caslon Text", Georgia, serif;
  }
  .card {
    position: absolute;
    left: 186px;
    width: 661px;
    height: 367px;
    overflow: hidden;
  }
  .card-front { top: 178px; background: var(--card-black); color: var(--ink-light); }
  .card-back  { top: 630px; background: var(--card-white); color: var(--ink-dark); }

  .card-front .name {
    position: absolute; left: 432px; top: 248px;
    font-size: 20px; letter-spacing: 0.3px;
  }
  .card-front .role-box {
    position: absolute; left: 430px; top: 282px;
    width: 240px; height: 36px;
    border: 1px solid var(--rule-light);
  }
  .card-front .role {
    position: absolute; left: 440px; top: 289px;
    font-size: 16px;
  }
  .card-front .email {
    position: absolute; left: 432px; top: 326px;
    font-size: 16px;
  }

  .card-back .quote { position: absolute; font-size: 16px; }
  .card-back .quote-open { left: 36px; top: 28px; }
  .card-back .quote-close { left: 337px; top: 314px; }
  .card-back .picture-frame {
    position: absolute; left: 36px; top: 59px;
    width: 589px; height: 250px;
    border: 1px solid var(--rule-dark);
  }
  .card-back .word-frame {
    position: absolute; left: 310px; top: 273px;
    width: 360px; height: 71px;
    border: 1px solid var(--rule-dark);
  }
  .card-back .website {
    position: absolute; left: 36px; top: 314px;
    font-size: 16px;
  }
  .card-back .social {
    position: absolute; left: 48px; top: 279px;
    display: flex; gap: 12px;
    font-size: 11px; color: var(--ink-dark);
  }
</style>
</head>
<body>
  <section class="card card-front" aria-label="Card front">
    <p class="name">samir t. kouri</p>
    <div class="role-box"></div>
    <p class="role">writer | photographer</p>
    <p class="email">get@samirkouri.com</p>
  </section>

  <section class="card card-back" aria-label="Card back">
    <p class="quote quote-open">a picture speaks a thousand words;</p>
    <div class="picture-frame"></div>
    <div class="word-frame"></div>
    <ul class="social" style="list-style:none">
      <li>pagenest</li>
      <li>snaplane</li>
      <li>lensroom</li>
    </ul>
    <p class="website">www.samirkouri.com</p>
    <p class="quote quote-close">a word draws a thousand pictures.</p>
  </section>
</body>
</html>
```